St bernard dog logo

LumoVale is a provider of Animal Assisted Therapy and Training for Special Education students.Was thinking of a St Bernard dog holding a young child's hand or a St Bernard wearing glasses as a front logo with the name LumoVale underneath, Lumo 1 color and Vale another color. Thought a pic of my 3 Therapy dogs and their names (Fenwick, Juno and Pippa) on the back of the card in a 1 color print. Can send pic of my dogs separately.

Target Market(s)

Families of special education students.

Industry/Entity Type

Physical Therapy

Contact Information for Business Card

TheraPetsDavid Small, OTR/L30776 N. Blackhawk TrailGrayslake, il 60417

Font styles to use
Sans Serif

Requirements
Must have
• St bernard dog holding young childs hand or st Bernard head wearing glasses.
• LumoVale name underneath. Lumo in 1 color Vale another.
Nice to have
• Something bold that would also look good on a tshirt.
Should not have
• Nudity or racism. That would be bad...

```html
<!DOCTYPE html>
<html lang="en">
<head>
<meta charset="utf-8">
<title>LumoVale Business Card</title>
<link rel="stylesheet" href="https://fonts.googleapis.com/css2?family=Open+Sans:wght@400;600;700&display=swap">
<style>
  :root {
    --slate: #474a51;
    --amber: #f7941d;
    --white: #ffffff;
    --paper: #ffffff;
    --ink: #111111;
    --shadow-ink: #2b2d31;
  }
  * { margin: 0; padding: 0; box-sizing: border-box; }
  html, body {
    width: 1015px;
    height: 1200px;
    overflow: hidden;
    background: var(--paper);
    font-family: "Open Sans", Arial, sans-serif;
  }
  .sheet { position: relative; width: 1015px; height: 1200px; }

  .card {
    position: absolute;
    left: 77px;
    width: 856px;
    height: 500px;
    background: var(--slate);
    overflow: hidden;
  }
  .card--front { top: 54px; }
  .card--back { top: 622px; height: 505px; }

  .side-label {
    position: absolute;
    left: 736px;
    font-size: 46px;
    font-weight: 400;
    color: var(--ink);
    line-height: 1;
  }
  .side-label--front { top: 564px; }
  .side-label--back { top: 1140px; }

  .hand-art {
    position: absolute;
    left: 75px;
    top: 118px;
    width: 317px;
    height: 146px;
    background: linear-gradient(100deg, rgba(247,148,29,0.15), rgba(247,148,29,0.45));
    border-radius: 60px 80px 70px 50px;
  }

  .wordmark {
    position: absolute;
    left: 419px;
    top: 250px;
    font-size: 61px;
    font-weight: 600;
    letter-spacing: -0.5px;
    line-height: 1;
    white-space: nowrap;
  }
  .wordmark__first { color: var(--white); }
  .wordmark__second { color: var(--amber); }

  .contact-band {
    position: absolute;
    left: 0;
    top: 0;
    width: 856px;
    height: 500px;
  }
  .contact-band path { fill: var(--amber); }

  .contact {
    position: absolute;
    left: 66px;
    top: 384px;
    font-size: 15.5px;
    line-height: 20px;
    color: var(--white);
    font-style: normal;
  }
  .contact__name { font-weight: 700; }
  .contact__name-second { color: var(--shadow-ink); }
  .contact__strong { font-weight: 600; }

  .dogs-art {
    position: absolute;
    left: 95px;
    top: 52px;
    width: 641px;
    height: 370px;
    background: var(--amber);
    border-radius: 140px 140px 30px 30px;
  }

  .dog-name {
    position: absolute;
    top: 428px;
    font-size: 40px;
    font-weight: 700;
    color: var(--amber);
    line-height: 1;
    transform: translateX(-50%);
  }
  .dog-name--1 { left: 230px; }
  .dog-name--2 { left: 429px; }
  .dog-name--3 { left: 612px; }
</style>
</head>
<body>
<main class="sheet">
  <section class="card card--front" aria-label="Card front">
    <div class="hand-art" role="img" aria-label="Line drawing of a child's hand resting in an open hand"></div>
    <div class="wordmark"><span class="wordmark__first">Lumo</span><span class="wordmark__second">Vale</span></div>
    <svg class="contact-band" viewBox="0 0 856 500" aria-hidden="true">
      <path d="M0,392 C60,366 160,360 260,376 C430,404 650,440 856,448 L856,500 L0,500 Z"/>
    </svg>
    <address class="contact">
      <div class="contact__name">Lumo<span class="contact__name-second">Vale</span></div>
      <div>Owen Marsh, OTR/L41852</div>
      <div>S. <span class="contact__strong">Cedarmoor LaneAshbrook,</span></div>
      <div>il 60417</div>
    </address>
  </section>
  <div class="side-label side-label--front">Front</div>

  <section class="card card--back" aria-label="Card back">
    <div class="dogs-art" role="img" aria-label="Silhouettes of three therapy dogs sitting side by side"></div>
    <div class="dog-name dog-name--1">Fenwick</div>
    <div class="dog-name dog-name--2">Juno</div>
    <div class="dog-name dog-name--3">Pippa</div>
  </section>
  <div class="side-label side-label--back">Back</div>
</main>
</body>
</html>
```